Mediapreneur looking for Wordpress Design for 55 plus community

I own the domain brightyearsahead.net and I have another contest going on to design the logo. I'm looking to build a site for those 55 plus who are living an active lifestyle.
I want to base my site off of this site, except make it more friendly to the 55 and over community.
http://www.kovaplume.com/
In my menu, I'd like to have the following categories. About Listen Read Watch Forum Contact and the ability to add more categories in the future (possible to external sites).
Listen will be podcasts, read will be blog posts, and watch will be videos (webinars)
Updates
I uploaded some images I bought from Pixelmarten that could be used in the design. Possibly a collage.
Videos are actually going to be webinars in the future. For example, I see a real estate agent presenting a webinar about active communities, or a financial adviser giving financial advice to my community. I was trying to simplify it for my audience, some of whom may not know what a webinar is, but I'd like to go with Webinar instead of Watch. I like read and listen, though. I plan on monetizing the site via sponsorship in podcasts and a directory of active communities I'm building. I'm possibly going to ask for sponsorship for webinars and write e-books in the future. Could you display podcasts on the home page? Maybe put the most recent blog posts below the podcasts? Also, can you put a form asking them to join my newsletter somewhere in prominent position? My call to actions are to get them to subscribe to my mailing list and listen to podcasts.
Thanks.
I changed my mind on using Webinar in the menu. I asked my mom what a webinar was and she gave me a blank look. I like the idea of using Watch instead. The menu should be in this order About Listen Read Watch Forum. Please put contact details in the header menu above the menu. Call...make up a phone number. Email..contact@brightyearsahead.net. In case you missed one of my previous public updates, Listen = Podcast, Read = Blog, and Watch = Webinar/Video.
Thanks and sorry for the changes.
55 and over
Build

```html
<!DOCTYPE html>
<html lang="en">
<head>
<meta charset="utf-8">
<title>Bright Years Ahead</title>
<link rel="stylesheet" href="https://fonts.googleapis.com/css2?family=Montserrat:wght@400;600;700;800&display=swap">
<style>
  :root {
    --green: #7dc242;
    --white: #ffffff;
    --ink: #2b2b2b;
    --muted: #5e5e5e;
    --intro-bg: #fafafa;
    --divider: #b9b39a;
    --sky-top: #3f7fb8;
    --sky-mid: #a9c6df;
    --hills: #5f8b8c;
    --valley: #4c7a3f;
    --haze: #f2d9b8;
    --forest: #3a4a2a;
    --forest-deep: #1f2e18;
  }
  * { box-sizing: border-box; margin: 0; padding: 0; }
  html, body { width: 1200px; height: 965px; overflow: hidden; }
  body { font-family: "Montserrat", sans-serif; color: var(--ink); background: var(--white); position: relative; }

  .hero { position: absolute; left: 0; top: 0; width: 1200px; height: 390px; overflow: hidden; }
  .hero-photo { position: absolute; inset: 0;
    background: linear-gradient(180deg, var(--sky-top) 0%, var(--sky-mid) 35%, #dfe8ee 48%, var(--hills) 60%, var(--valley) 85%, #3f6a35 100%); }
  .brand { position: absolute; left: 245px; top: 26px; display: flex; align-items: center; gap: 8px;
    color: var(--white); font-weight: 700; font-size: 15px; line-height: 1; }
  .brand-dot { width: 12px; height: 12px; border-radius: 50%; background: var(--green); }
  .main-nav { position: absolute; top: 35px; left: 640px; display: flex; gap: 0; }
  .main-nav a { color: var(--white); text-decoration: none; font-size: 11.5px; font-weight: 600; margin-right: 26px; position: relative; }
  .main-nav a.current::after { content: ""; position: absolute; left: 5px; right: 5px; bottom: -6px; height: 1px; background: var(--white); }
  .hero-title { position: absolute; top: 122px; left: 0; width: 1200px; text-align: center;
    color: var(--white); font-size: 41px; font-weight: 700; letter-spacing: -0.5px; }
  .hero-sub { position: absolute; top: 178px; left: 0; width: 1200px; text-align: center;
    color: var(--white); font-size: 10px; font-weight: 600; }
  .cta { position: absolute; left: 518px; top: 222px; width: 164px; height: 40px; background: var(--green);
    color: var(--white); font-size: 17px; font-weight: 600; text-align: center; line-height: 40px; text-decoration: none; }

  .intro { position: absolute; left: 0; top: 390px; width: 1200px; height: 252px; background: var(--intro-bg); }
  .intro-lead { position: absolute; top: 30px; left: 360px; width: 480px; text-align: center;
    font-size: 14px; line-height: 18px; color: var(--ink); }
  .intro-col { position: absolute; top: 124px; width: 330px; font-size: 10.2px; line-height: 18.8px; color: var(--muted); }
  .intro-col h3 { font-size: 10.5px; font-weight: 400; color: var(--ink); line-height: 14px; margin-bottom: 4px; }
  .intro-col.left { left: 243px; }
  .intro-col.right { left: 641px; }
  .intro-divider { position: absolute; left: 604px; top: 120px; width: 1px; height: 96px; background: var(--divider); }

  .newsletter { position: absolute; left: 0; top: 642px; width: 1200px; height: 245px; overflow: hidden; }
  .newsletter-photo { position: absolute; inset: 0;
    background: linear-gradient(100deg, var(--haze) 0%, #c9a27a 20%, var(--forest) 50%, var(--forest-deep) 100%); }
  .mail-icon { position: absolute; left: 415px; top: 42px; }
  .newsletter-title { position: absolute; left: 551px; top: 43px; color: var(--white);
    font-size: 28px; font-weight: 700; line-height: 36px; }
  .signup { position: absolute; left: 414px; top: 160px; display: flex; }
  .signup input { width: 269px; height: 34px; border: 0; border-radius: 2px 0 0 2px; padding-left: 14px;
    font-family: "Montserrat", sans-serif; font-size: 10px; color: var(--muted); background: var(--white); }
  .signup input::placeholder { color: #9a9a9a; }
  .signup button { width: 103px; height: 34px; border: 0; border-radius: 0 2px 2px 0; background: var(--green);
    display: flex; align-items: center; justify-content: center; }

  .footer-nav { position: absolute; left: 0; top: 887px; width: 1200px; height: 78px; background: var(--white);
    display: flex; justify-content: center; align-items: center; }
  .footer-nav a { color: var(--ink); text-decoration: none; font-size: 11.2px; text-transform: uppercase; margin: 0 13px; }
</style>
</head>
<body>
  <header class="hero">
    <div class="hero-photo" role="img" aria-label="Photo of a man with arms spread wide overlooking green mountains under a blue, cloudy sky"></div>
    <div class="brand"><span class="brand-dot"></span>Bright Years Ahead</div>
    <nav class="main-nav">
      <a class="current" href="#">About</a>
      <a href="#">Listen</a>
      <a href="#">Read</a>
      <a href="#">Watch</a>
      <a href="#">Forum</a>
      <a href="#">Contact</a>
    </nav>
    <h1 class="hero-title">LIFE IS BEAUTIFULL</h1>
    <p class="hero-sub">Lorem ipsum dolor sit amet, consectetur adipiscing elit, sed do eiusmod tempor incididunt</p>
    <a class="cta" href="#">Start now</a>
  </header>

  <section class="intro">
    <p class="intro-lead">Company has been delivering results since we opened in 2014. Our goal is to provide both a superior customer experience and tremendous value for our customers.</p>
    <div class="intro-col left">
      <h3>But I must explain</h3>
      <p>to you how all this mistaken idea of denouncing pleasure and praising pain was born and I will give you a complete account of the system, and expound the actual teachings of the great explorer of the truth, the master-builder of human happiness. No</p>
    </div>
    <div class="intro-divider"></div>
    <div class="intro-col right">
      <h3>Which of us ever undertakes</h3>
      <p>laborious physical exercise, except to obtain some advantage from it? But who has any right to find fault with a man who chooses to enjoy a pleasure that has no annoying consequences, or one who avoids a pain that produces no</p>
    </div>
  </section>

  <section class="newsletter">
    <div class="newsletter-photo" role="img" aria-label="Photo of a misty pine forest valley at sunrise"></div>
    <svg class="mail-icon" width="105" height="76" viewBox="0 0 105 76" aria-hidden="true">
      <rect x="3.5" y="3.5" width="98" height="69" rx="2" fill="none" stroke="#ffffff" stroke-width="7"/>
      <polyline points="17,20 52,40 88,20" fill="none" stroke="#ffffff" stroke-width="7" stroke-linejoin="round"/>
    </svg>
    <h2 class="newsletter-title">Subscribe<br>to our newsletter</h2>
    <form class="signup">
      <input type="email" placeholder="Email">
      <button type="button" aria-label="Subscribe">
        <svg width="34" height="20" viewBox="0 0 34 20" aria-hidden="true">
          <line x1="1" y1="10" x2="32" y2="10" stroke="#ffffff" stroke-width="1.6"/>
          <polyline points="23,1.5 32,10 23,18.5" fill="none" stroke="#ffffff" stroke-width="1.6"/>
        </svg>
      </button>
    </form>
  </section>

  <nav class="footer-nav">
    <a href="#">About</a>
    <a href="#">Listen</a>
    <a href="#">Read</a>
    <a href="#">Watch</a>
    <a href="#">Forum</a>
    <a href="#">Contact</a>
  </nav>
</body>
</html>
```